Corvella Paintless Dent Removal

Our company works on vehicles removing dents using a highly skilled trade which the metal is massaged out with special tools without disturbing the original paint, hence paintless dent removal. Besides keeping the paint and metal original its also very environmentally friendly since no paint or toxic fillers are used. Also we we are one of the most experienced companies in the business with 25 years

Target Market(s)

Retail Automobile consumers, Auto Dealerships and Auto Body Shops

Industry/Entity Type

Auto Repair

Contact Information for Business Card

Dennis Holbrook
PO Box 538 Ashmere, NY 11952
631-472-8816
corvellapdr@mailnest.example
website corvellapdr.example
youtube corvella paintless dent removal
25 years of experience removing Dents, Dings and Hail Damage

Font styles to use
Serif
Sans Serif

Colors

Designer to choose colors to be used in the design.

Requirements
Must have
• I do like things that are simple but classy and somewhat bold, also I like my logo so that should be somewhat important

```html
<!DOCTYPE html>
<html lang="en">
<head>
<meta charset="utf-8">
<title>Corvella Paintless Dent Removal – Business Card</title>
<link rel="stylesheet" href="https://fonts.googleapis.com/css2?family=Roboto:wght@400;700;900&family=Roboto+Condensed:wght@400&display=swap">
<style>
  :root {
    --backdrop: #2a2a2a;
    --card-white: #f7f7f5;
    --brand-navy: #1c2b5a;
    --brand-green: #7cc414;
    --text-grey: #555a60;
    --rule-grey: #9a9a9a;
    --badge-gold: #d9a531;
    --badge-dark: #1d1d1d;
    --white: #ffffff;
  }
  * { box-sizing: border-box; margin: 0; padding: 0; }
  html, body {
    width: 1200px; height: 911px; overflow: hidden;
    background: var(--backdrop);
    font-family: "Roboto", Arial, sans-serif;
  }
  .canvas { position: relative; width: 1200px; height: 911px; }

  .card {
    position: absolute;
    width: 520px; height: 297px;
    box-shadow: 0 14px 30px rgba(0,0,0,.45);
    overflow: hidden;
  }

  /* Front */
  .card-front { left: 70px; top: 150px; background: var(--card-white); }
  .front-brand {
    position: absolute; left: 40px; top: 56px;
    display: flex; align-items: center; gap: 12px;
  }
  .brand-dot {
    width: 34px; height: 34px; border-radius: 50%;
    background: var(--brand-green); flex: none;
  }
  .brand-name {
    font-weight: 900; color: var(--brand-navy);
    font-size: 22px; line-height: 1.15; text-transform: uppercase;
    letter-spacing: .5px; max-width: 260px;
  }
  .name-rule {
    position: absolute; left: 36px; right: 36px; top: 172px;
    display: flex; align-items: center; gap: 14px;
  }
  .name-rule::before, .name-rule::after {
    content: ""; flex: 1; height: 1px; background: var(--rule-grey);
  }
  .person-name {
    font-family: "Roboto Condensed", Arial, sans-serif;
    font-size: 19px; color: var(--brand-navy);
    text-transform: uppercase; letter-spacing: .5px;
  }
  .contact-list {
    position: absolute; left: 40px; bottom: 30px;
    list-style: none; font-family: "Roboto Condensed", Arial, sans-serif;
    font-size: 13px; color: var(--text-grey); line-height: 1.55;
  }
  .contact-list li { display: flex; align-items: center; gap: 7px; }
  .contact-list svg { width: 11px; height: 11px; fill: var(--brand-navy); flex: none; }
  .mailing-address {
    position: absolute; right: 40px; bottom: 30px; text-align: right;
    font-family: "Roboto Condensed", Arial, sans-serif;
    font-size: 13px; color: var(--text-grey); line-height: 1.55;
  }

  /* Back */
  .card-back { left: 610px; top: 450px; background: var(--brand-green); }
  .back-brand {
    position: absolute; left: 34px; top: 34px; color: var(--white);
  }
  .back-brand .brand-name {
    color: var(--white); font-size: 30px; max-width: 300px; line-height: 1.05;
  }
  .back-web {
    margin-top: 8px; font-size: 14px; letter-spacing: 3px;
  }
  .years-badge {
    position: absolute; right: 26px; top: 22px;
    width: 58px; height: 58px; border-radius: 50%;
    background: var(--badge-dark); border: 4px solid var(--badge-gold);
  }
</style>
</head>
<body>
<main class="canvas">

  <section class="card card-front" aria-label="Business card front">
    <div class="front-brand">
      <span class="brand-dot" aria-hidden="true"></span>
      <span class="brand-name">Corvella Paintless Dent Removal</span>
    </div>

    <div class="name-rule"><span class="person-name">Dennis Holbrook</span></div>

    <ul class="contact-list">
      <li><svg viewBox="0 0 24 24" aria-hidden="true"><path d="M6.6 10.8a15 15 0 0 0 6.6 6.6l2.2-2.2a1 1 0 0 1 1-.25 11.4 11.4 0 0 0 3.6.57 1 1 0 0 1 1 1V20a1 1 0 0 1-1 1A17 17 0 0 1 3 4a1 1 0 0 1 1-1h3.5a1 1 0 0 1 1 1c0 1.25.2 2.45.57 3.6a1 1 0 0 1-.25 1z"/></svg>631-472-8816</li>
      <li><svg viewBox="0 0 24 24" aria-hidden="true"><path d="M2 5h20v14H2z M3.5 6.5 12 13l8.5-6.5" stroke="#fff" stroke-width="1.5"/></svg>corvellapdr@mailnest.example</li>
      <li><svg viewBox="0 0 24 24" aria-hidden="true"><rect x="2" y="4" width="20" height="16" rx="3"/></svg>corvella paintless dent removal</li>
    </ul>

    <address class="mailing-address" style="font-style:normal">
      PO Box 538<br>Ashmere, NY 11952<br>www.corvellapdr.example
    </address>
  </section>

  <section class="card card-back" aria-label="Business card back">
    <div class="back-brand">
      <div class="brand-name">Corvella Paintless Dent Removal</div>
      <div class="back-web">corvellapdr.example</div>
    </div>
    <span class="years-badge" aria-hidden="true"></span>
  </section>

</main>
</body>
</html>
```